Bref créative
Valcourt Chiropractic
Business card, letterhead, envelope
Professional
Valcourt Chiropractic (use logo)
41785 Brookhaven Rd
Oakridge Twp, MI 48193
info@ValcourtChiroExample.com
www.ValcourtChiroExample.com
Want a design that portrays health and wellness in a professional manner
(in bullet format)
-We Specialize in Improving Health & Wellness Naturally
-Most Insurances Accepted
-Holistic Family Health Care
-Massage Therapist on Staff

```html
<!DOCTYPE html>
<html lang="en">
<head>
<meta charset="utf-8">
<title>Valcourt Chiropractic Stationery</title>
<link rel="stylesheet" href="https://fonts.googleapis.com/css2?family=Marcellus&family=Open+Sans:wght@400;600&display=swap">
<style>
:root{
  --stage:#2a2a2c;
  --paper:#ffffff;
  --paper-shade:#f1f3f6;
  --blue:#1d3d8f;
  --green:#6cb33f;
  --ink:#1f3a8a;
  --grey:#8a8f98;
  --rule:#c9ccd2;
  --band-text:#e3e9f6;
}
*{margin:0;padding:0;box-sizing:border-box}
html,body{width:1200px;height:499px;overflow:hidden;background:var(--stage)}
body{position:relative;font-family:"Open Sans",Arial,sans-serif;color:var(--grey)}
.sheet{position:absolute;background:var(--paper);box-shadow:0 3px 10px rgba(0,0,0,.5);overflow:hidden}

/* straight footer band: thin green rule above a solid blue strip */
.band{position:absolute;left:0;right:0;bottom:0;background:var(--blue);border-top:3px solid var(--green)}

.brand{display:flex;align-items:center;gap:6px;font-family:"Marcellus",Georgia,serif;color:var(--ink);line-height:1.05}
.brand-dot{flex:none;border-radius:50%;background:var(--green)}
.brand-dot.lg{width:16px;height:16px}
.brand-dot.md{width:13px;height:13px}
.brand-dot.sm{width:7px;height:7px}

.letterhead{left:12px;top:12px;width:204px;height:372px}
.fax-sheet{left:235px;top:12px;width:204px;height:372px}
.letterhead .brand,.fax-sheet .brand{position:absolute;left:14px;top:14px;font-size:15px}
.sheet .band.tall{height:28px}
.sheet-footer{position:absolute;left:12px;right:12px;bottom:6px;display:flex;justify-content:space-between;font-size:5px;color:var(--band-text);line-height:1.5;white-space:nowrap}
.sheet-footer span:last-child{text-align:right}

.fax-title{position:absolute;left:14px;top:62px;font-size:14px;font-weight:600;color:#333;letter-spacing:.5px}
.fax-fields{position:absolute;left:14px;right:14px;top:86px;display:grid;grid-template-columns:1fr 1fr;column-gap:14px;row-gap:7px;font-size:4.5px;color:#555}
.fax-fields span{border-bottom:.6px solid var(--rule);padding-bottom:1px}
.fax-checks{position:absolute;left:14px;right:14px;top:140px;display:grid;grid-template-columns:repeat(5,1fr);font-size:4px;color:#555;white-space:nowrap}
.fax-checks span::before{content:"";display:inline-block;width:5px;height:5px;border:.6px solid #777;margin-right:2px;vertical-align:middle}

.envelope{width:390px;height:160px}
.envelope.back{left:739px;top:40px;background:var(--paper-shade)}
.envelope.front{left:800px;top:84px}
.envelope .brand{position:absolute;left:14px;top:14px;font-size:13px}
.envelope .band{height:30px}
.envelope .web{position:absolute;right:14px;bottom:10px;font-size:5px;color:var(--band-text)}

.card{width:120px;height:60px}
.card .brand{position:absolute;left:7px;top:7px;font-size:6.5px}
.card .band{height:16px;border-top-width:2px}
.card-a{left:744px;top:356px}
.card-b{left:883px;top:356px}
.card-c{left:744px;top:428px}
.card-d{left:883px;top:428px;background:var(--blue)}
.card-list{position:absolute;left:7px;top:9px;font-size:3.8px;line-height:1.6;color:#555;list-style:none}
.card-d .card-list{color:var(--band-text)}
.card-mark{position:absolute;right:10px;top:16px;width:26px;height:26px;border-radius:50%;background:var(--paper-shade)}
.card-d .card-mark{background:rgba(255,255,255,.14)}
.card-contact{position:absolute;right:6px;bottom:3px;font-size:3.6px;color:var(--band-text);text-align:right;line-height:1.4;white-space:nowrap}
</style>
</head>
<body>

<section class="sheet letterhead" aria-label="Letterhead">
  <div class="brand"><span class="brand-dot lg"></span><span>Valcourt<br>Chiropractic</span></div>
  <div class="band tall"></div>
  <div class="sheet-footer"><span>41785 Brookhaven Rd<br>Oakridge Twp, MI 48193</span><span>P (586) 555-0142<br>info@ValcourtChiroExample.com</span></div>
</section>

<section class="sheet fax-sheet" aria-label="Fax cover sheet">
  <div class="brand"><span class="brand-dot lg"></span><span>Valcourt<br>Chiropractic</span></div>
  <h1 class="fax-title">FAX</h1>
  <div class="fax-fields"><span>To:</span><span>From:</span><span>Fax:</span><span>Pages:</span><span>Phone:</span><span>Date:</span><span>Re:</span><span>CC:</span></div>
  <div class="fax-checks"><span>Urgent</span><span>For Review</span><span>Comment</span><span>Reply</span><span>Recycle</span></div>
  <div class="band tall"></div>
  <div class="sheet-footer"><span>41785 Brookhaven Rd<br>Oakridge Twp, MI 48193</span><span>F (586) 555-0143<br>www.ValcourtChiroExample.com</span></div>
</section>

<section class="sheet envelope back" aria-label="Envelope back">
  <div class="brand"><span class="brand-dot md"></span><span>Valcourt<br>Chiropractic</span></div>
</section>

<section class="sheet envelope front" aria-label="Envelope front">
  <div class="brand"><span class="brand-dot md"></span><span>Valcourt<br>Chiropractic</span></div>
  <div class="band"></div>
  <div class="web">www.ValcourtChiroExample.com</div>
</section>

<section class="sheet card card-a" aria-label="Business card front">
  <div class="brand"><span class="brand-dot sm"></span><span>Valcourt<br>Chiropractic</span></div>
  <div class="band"></div>
  <div class="card-contact">Dr. R. Valcourt<br>(586) 555-0142</div>
</section>

<section class="sheet card card-b" aria-label="Business card front alternate">
  <div class="brand"><span class="brand-dot sm"></span><span>Valcourt<br>Chiropractic</span></div>
  <div class="band"></div>
  <div class="card-contact">www.ValcourtChiroExample.com</div>
</section>

<section class="sheet card card-c" aria-label="Business card back">
  <ul class="card-list"><li>• We Specialize in Improving Health &amp; Wellness Naturally</li><li>• Most Insurances Accepted</li><li>• Holistic Family Health Care</li><li>• Massage Therapist on Staff</li></ul>
  <span class="card-mark"></span>
</section>

<section class="sheet card card-d" aria-label="Business card back alternate">
  <ul class="card-list"><li>• We Specialize in Improving Health &amp; Wellness Naturally</li><li>• Most Insurances Accepted</li><li>• Holistic Family Health Care</li><li>• Massage Therapist on Staff</li></ul>
  <span class="card-mark"></span>
</section>

</body>
</html>
```